Brightfield Yard Service and Beyond LLC

• Mowing
• Weed eating
•Edging
• hedge trimming
• landscaping
•mulching
•yard clean up
• pressure washing

Target Market(s)

Everyone

Contact Information for Business Card

Licensed and insured

Font styles to use
Serif

Colors
59FF00
82FF00
B8FF75
E3FFCB
F4FFEA
F0912C
F2A743
F7CA91
FBE8D2
FDF5EE
EE7325
F08F49
F5BC92
FAE3D3
FDF4ED
EB3D1F
EC4F4E
F09395
F8D3D4
FCEDEE
E54698
E96AAD
F1A4CE
F9D9EA
FCEFF6

```html
<!DOCTYPE html>
<html lang="en">
<head>
<meta charset="utf-8">
<title>Brightfield Yard Service and Beyond LLC – Business Card</title>
<link rel="stylesheet" href="https://fonts.googleapis.com/css2?family=Montserrat:wght@400;500;600&display=swap">
<style>
  :root {
    --page: #ece8e1;
    --card-white: #ffffff;
    --green-deep: #1f9a43;
    --green-mid: #34a04d;
    --green-light: #7dbb4a;
    --lime: #8cc63f;
    --ink: #2a2a2a;
    --white: #ffffff;
  }
  * { margin: 0; padding: 0; box-sizing: border-box; }
  html, body { width: 900px; height: 1200px; overflow: hidden; }
  body {
    background: var(--page);
    font-family: "Montserrat", Arial, sans-serif;
    color: var(--ink);
    position: relative;
  }
  .card {
    position: absolute;
    left: 80px;
    width: 742px;
    height: 442px;
    border-radius: 28px;
    overflow: hidden;
    box-shadow: 0 6px 14px rgba(0,0,0,0.28);
  }
  .card--front { top: 130px; background: var(--card-white); }
  .card--back {
    top: 638px;
    background: linear-gradient(90deg, var(--green-mid) 0%, #3ea34d 45%, var(--green-light) 100%);
    color: var(--white);
  }
  .brand-name {
    position: absolute;
    width: 440px;
    text-align: center;
    font-weight: 600;
    font-size: 29px;
    line-height: 36px;
  }
  .card--front .brand-name { left: 36px; top: 42px; color: var(--green-deep); }
  .card--back .brand-name { left: 46px; top: 56px; color: var(--white); }

  .owner { position: absolute; left: 40px; top: 188px; }
  .owner__name { font-size: 26px; font-weight: 600; color: var(--green-deep); line-height: 32px; }
  .owner__role { font-size: 18px; line-height: 24px; }

  .contact-list { position: absolute; left: 44px; top: 257px; list-style: none; }
  .contact-list li { display: flex; align-items: center; height: 25.5px; font-size: 18px; }
  .contact-list svg { width: 15px; height: 15px; margin-right: 13px; fill: var(--green-deep); }

  .address { position: absolute; left: 46px; top: 349px; font-size: 18px; line-height: 22px; }

  .footer-bands { position: absolute; left: 0; top: 0; width: 742px; height: 442px; }
  .licence-note {
    position: absolute; right: 26px; top: 406px;
    font-size: 18px; color: var(--white);
  }

  .services { position: absolute; left: 34px; top: 175px; }
  .services__title { font-size: 22px; font-weight: 600; margin-bottom: 14px; }
  .services__list { list-style: none; }
  .services__list li {
    font-size: 20px; line-height: 23px; padding-left: 19px; position: relative;
  }
  .services__list li::before {
    content: ""; position: absolute; left: 2px; top: 8px;
    width: 9px; height: 9px; border-radius: 50%; background: var(--lime);
  }
</style>
</head>
<body>
  <section class="card card--front">
    <div class="brand-name">Brightfield Yard Service<br>and Beyond LLC</div>

    <div class="owner">
      <div class="owner__name">Daniel Harlow</div>
      <div class="owner__role">Owner</div>
    </div>

    <ul class="contact-list">
      <li><svg viewBox="0 0 16 16"><path d="M1 6c0-2 3-3 7-3s7 1 7 3v1h-3V5.5H4V7H1zM3 8h10l1 6H2z"/></svg>(555) 014-2290</li>
      <li><svg viewBox="0 0 16 16"><path d="M1 3h14v1.5L8 9 1 4.5zM1 6l7 4.5L15 6v7H1z"/></svg>hello@brightfieldyard.com</li>
      <li><svg viewBox="0 0 16 16"><circle cx="8" cy="8" r="7"/><path d="M4 5l3 1 0 3-2 1zM9 9l3-1 1 3-3 2z" fill="#fff"/></svg>www.brightfieldyard.com</li>
    </ul>

    <div class="address">4820 Maple Row, City<br>State, 55021</div>

    <svg class="footer-bands" viewBox="0 0 742 442" aria-hidden="true">
      <polygon points="0,425 400,425 397,442 0,442" fill="var(--lime)"/>
      <polygon points="420,390 496,390 470,442 394,442" fill="var(--lime)"/>
      <polygon points="496,390 742,388 742,442 470,442" fill="#ffffff"/>
      <polygon points="503,390 742,388 742,442 478,442" fill="var(--green-deep)"/>
      <path d="M432 413 l8 8 l15 -17" stroke="#fff" stroke-width="5" fill="none" stroke-linecap="round" stroke-linejoin="round"/>
    </svg>
    <div class="licence-note">Licensed and insured</div>
  </section>

  <section class="card card--back">
    <div class="brand-name">Brightfield Yard Service<br>and Beyond LLC</div>
    <div class="services">
      <h2 class="services__title">Our Services</h2>
      <ul class="services__list">
        <li>Mowing</li>
        <li>Weed eating</li>
        <li>Edging</li>
        <li>Hedge trimming</li>
        <li>Landscaping</li>
        <li>Mulching</li>
        <li>Yard clean up</li>
        <li>Pressure washing</li>
      </ul>
    </div>
  </section>
</body>
</html>
```